Dale Merrow Broker owner of Real Estate Company

Dale Merrow, GRI CRS ABR
Broker Owner
586-317-4902
dalemerrow@dalemerrowrealtors.example
14637 Larkspur Ave. St. Harbor Pointe, MI 48190
Licensed in Michigan and Florida
"37 Years of Outstanding Service based on a Result Driven Marketing Plan"

```html
<!DOCTYPE html>
<html lang="en">
<head>
<meta charset="utf-8">
<title>Dale Merrow Realtors – Business Card</title>
<link href="https://fonts.googleapis.com/css2?family=Poppins:wght@400;500;600;700&display=swap" rel="stylesheet">
<style>
  :root {
    --navy: #0b2272;
    --white: #ffffff;
    --ink: #3b3b3b;
    --grey-line: #a3a3a3;
    --stage: #3a3a3c;
    --rule-light: rgba(255,255,255,.45);
  }
  * { margin: 0; padding: 0; box-sizing: border-box; }
  html, body {
    width: 1200px; height: 866px; overflow: hidden;
    background: var(--stage);
    font-family: "Poppins", sans-serif;
  }
  .sheet {
    width: 1200px; height: 866px;
    display: flex; align-items: center; justify-content: center; gap: 40px;
  }
  .card {
    position: relative;
    width: 560px; height: 320px;
    overflow: hidden;
    box-shadow: 0 10px 24px rgba(0,0,0,.35);
  }

  /* Front */
  .card-front { background: var(--white); color: var(--navy); }
  .brand-name {
    position: absolute; left: 36px; top: 30px;
    font-size: 24px; font-weight: 600; letter-spacing: 1px;
    text-transform: uppercase; color: var(--navy); white-space: nowrap;
  }
  .brand-rule {
    position: absolute; left: 36px; top: 74px; width: 300px; height: 1px;
    background: var(--navy); opacity: .5;
  }
  .agent { position: absolute; left: 36px; top: 86px; }
  .agent-name { font-size: 15px; font-weight: 700; text-transform: uppercase; white-space: nowrap; }
  .agent-name span { font-weight: 500; }
  .agent-title { font-size: 13px; color: var(--ink); }
  .divider {
    position: absolute; left: 36px; top: 132px; width: 300px; height: 1px;
    background: var(--navy);
  }
  .contacts { position: absolute; left: 36px; top: 142px; list-style: none; }
  .contacts li {
    display: flex; align-items: center; gap: 8px;
    font-size: 12px; color: var(--ink); line-height: 20px; white-space: nowrap;
  }
  .contacts svg { width: 12px; height: 12px; flex: none; }
  .portrait {
    position: absolute; left: 364px; top: 92px; width: 164px; height: 132px;
    background: radial-gradient(circle at 55% 45%, #7b7060 0%, #4c473d 55%, #2f2d2a 100%);
  }
  .address-rule {
    position: absolute; left: 364px; top: 234px; width: 164px; height: 1px;
    background: var(--navy); opacity: .6;
  }
  .address {
    position: absolute; right: 32px; top: 240px; text-align: right;
    font-size: 12px; color: var(--ink); line-height: 16px; white-space: nowrap;
  }
  .front-band { position: absolute; left: 0; bottom: 0; width: 560px; height: 40px; }

  /* Back */
  .card-back {
    background: var(--navy);
    color: var(--white);
    display: flex; flex-direction: column; align-items: center; justify-content: center;
    text-align: center;
  }
  .back-brand {
    font-size: 28px; font-weight: 600; letter-spacing: 1.5px; text-transform: uppercase; white-space: nowrap;
  }
  .back-rule { width: 380px; height: 1px; background: var(--rule-light); margin: 16px 0 16px; }
  .licence { font-size: 14px; }
  .tagline { font-size: 14px; line-height: 20px; margin-top: 4px; }
  .back-rule-bottom { width: 380px; height: 1px; background: var(--rule-light); margin-top: 16px; }
</style>
</head>
<body>
<main class="sheet">

  <section class="card card-front" aria-label="Business card front">
    <div class="brand-name">Dale Merrow Realtors</div>
    <div class="brand-rule"></div>

    <div class="agent">
      <div class="agent-name">Dale Merrow, <span>GRI CRS ABR</span></div>
      <div class="agent-title">Broker Owner</div>
    </div>
    <div class="divider"></div>

    <ul class="contacts">
      <li>
        <svg viewBox="0 0 24 24" fill="var(--navy)"><path d="M6.6 10.8a15.1 15.1 0 0 0 6.6 6.6l2.2-2.2a1 1 0 0 1 1-.25 11.4 11.4 0 0 0 3.6.57 1 1 0 0 1 1 1V20a1 1 0 0 1-1 1A17 17 0 0 1 3 4a1 1 0 0 1 1-1h3.5a1 1 0 0 1 1 1c0 1.25.2 2.45.57 3.6a1 1 0 0 1-.25 1z"/></svg>
        586-317-4902
      </li>
      <li>
        <svg viewBox="0 0 24 24" fill="var(--navy)"><path d="M2 5h20v14H2z"/><path d="M2 5l10 8 10-8" fill="none" stroke="#fff" stroke-width="1.6"/></svg>
        dalemerrow@dalemerrowrealtors.example
      </li>
      <li>
        <svg viewBox="0 0 24 24" fill="none" stroke="var(--navy)" stroke-width="2"><circle cx="12" cy="12" r="9"/><path d="M3 12h18M12 3c3 3 3 15 0 18M12 3c-3 3-3 15 0 18"/></svg>
        www.dalemerrowrealtors.example
      </li>
    </ul>

    <div class="portrait" role="img" aria-label="Portrait photograph of Dale Merrow"></div>

    <div class="address-rule"></div>
    <div class="address">14637 Larkspur Ave.<br>Harbor Pointe, MI 48190</div>

    <svg class="front-band" viewBox="0 0 560 40" preserveAspectRatio="none" aria-hidden="true">
      <path d="M0 12 L150 30 C165 32 172 24 190 25 L560 30 L560 40 L0 40 Z" fill="var(--navy)"/>
      <path d="M0 6 L150 24" stroke="var(--grey-line)" stroke-width="3" fill="none"/>
    </svg>
  </section>

  <section class="card card-back" aria-label="Business card back">
    <div class="back-brand">Dale Merrow Realtors</div>
    <div class="back-rule"></div>
    <p class="licence">Licensed in Michigan and Florida</p>
    <p class="tagline">37 Years of Outstanding Service based<br>on a Result Driven Marketing Plan</p>
    <div class="back-rule-bottom"></div>
  </section>

</main>
</body>
</html>
```